Design business card using existing logo.

PLEASE DO NOT USE "RED WHITE & BLACK" color combo! Thank you.

Try different color combos such as:
- Vintage colors like brown, orange, gold, blue (not all together but a combo of 1 or 3
- Blue, w/ grey, or silver or white, Blue monochromatic can work as well.
- Use monochromatic variations on back (just an idea)

- Include full name, "Quillmark Records" on at least one side.

Target Market(s)

Teens

Industry/Entity Type

Business

Colors
3277b5
ffc214
f04a50
f78f20

```html
<!DOCTYPE html>
<html lang="en">
<head>
<meta charset="utf-8">
<title>Quillmark Records – Business Card</title>
<link rel="stylesheet" href="https://fonts.googleapis.com/css2?family=Montserrat:wght@400;500&family=Open+Sans:wght@400;700&display=swap">
<style>
  :root {
    --stage: #e6e9ee;
    --navy: #1f3f63;
    --navy-deep: #183450;
    --navy-mark: #14293f;
    --blue: #3277b5;
    --silver-top: #ffffff;
    --silver-bottom: #e6eaef;
    --ink: #2b3440;
  }
  * { box-sizing: border-box; margin: 0; padding: 0; }
  html, body { width: 1200px; height: 900px; overflow: hidden; }
  body {
    background: var(--stage);
    font-family: "Open Sans", Arial, sans-serif;
    position: relative;
  }
  .card {
    position: absolute;
    left: 232px;
    width: 736px;
    height: 420px;
    border-radius: 22px;
    overflow: hidden;
  }
  .card-back {
    top: 20px;
    background: linear-gradient(160deg, var(--navy) 0%, var(--navy-deep) 100%);
  }
  .card-front {
    top: 460px;
    background: linear-gradient(160deg, var(--silver-top) 0%, var(--silver-bottom) 100%);
  }

  /* back */
  .back-mark {
    position: absolute;
    left: 50%; top: 50%;
    transform: translate(-50%, -50%);
    display: flex; align-items: center; gap: 14px;
  }
  .back-mark .dot {
    width: 34px; height: 34px; border-radius: 50%;
    border: 3px solid var(--navy-mark);
  }
  .back-mark .name {
    font-family: "Montserrat", Arial, sans-serif;
    font-weight: 500; font-size: 26px; letter-spacing: 3px;
    color: var(--navy-mark);
  }

  /* front */
  .band { position: absolute; top: 60px; height: 72px; }
  .band-left { left: 0; width: 50%; background: var(--navy); }
  .band-right { right: 0; width: 50%; background: var(--blue); }
  .badge {
    position: absolute; left: 50%; top: 42px;
    width: 108px; height: 108px; margin-left: -54px;
    border-radius: 50%;
    background: var(--silver-top);
    border: 14px solid var(--navy);
  }
  .brand {
    position: absolute; top: 170px; width: 100%;
    text-align: center;
    font-family: "Montserrat", Arial, sans-serif;
    font-weight: 500; font-size: 30px; letter-spacing: 2px;
    color: var(--navy);
  }
  .person { position: absolute; top: 222px; width: 100%; text-align: center; }
  .person-name { font-weight: 700; font-size: 24px; color: var(--blue); line-height: 1.1; }
  .person-role { font-size: 17px; color: var(--ink); }

  .details {
    position: absolute; top: 290px; left: 0; width: 100%;
    display: flex; justify-content: center; align-items: stretch;
    font-size: 17px; color: var(--ink); line-height: 1.5;
  }
  .address { text-align: right; padding-right: 26px; font-style: normal; }
  .divider { width: 2px; background: var(--ink); }
  .contact { padding-left: 26px; list-style: none; }
  .contact li { display: flex; align-items: center; gap: 10px; }
  .contact svg { width: 16px; height: 16px; flex: none; }
</style>
</head>
<body>
  <section class="card card-back">
    <div class="back-mark">
      <span class="dot"></span>
      <span class="name">QUILLMARK</span>
    </div>
  </section>

  <section class="card card-front">
    <div class="band band-left"></div>
    <div class="band band-right"></div>
    <div class="badge"></div>
    <h1 class="brand">QUILLMARK RECORDS</h1>
    <div class="person">
      <p class="person-name">Dana Whitlow</p>
      <p class="person-role">Manager</p>
    </div>
    <div class="details">
      <address class="address">
        12 Harbor Lane, Mill Road<br>
        West Quarry side<br>
        CA 902114
      </address>
      <div class="divider"></div>
      <ul class="contact">
        <li>
          <svg viewBox="0 0 16 16" aria-hidden="true"><path fill="#3277b5" d="M3.5 1.5l2.2 2.6-1.2 1.7a9 9 0 0 0 5.7 5.7l1.7-1.2 2.6 2.2-1.5 2A12 12 0 0 1 1.5 3z"/></svg>
          +000 4821 7730
        </li>
        <li>
          <svg viewBox="0 0 16 16" aria-hidden="true"><rect x="1" y="3" width="14" height="10" rx="1.5" fill="#3277b5"/><path d="M1.5 4l6.5 5 6.5-5" stroke="#fff" stroke-width="1.4" fill="none"/></svg>
          hello@quillmark.com
        </li>
        <li>
          <svg viewBox="0 0 16 16" aria-hidden="true"><circle cx="8" cy="8" r="6.5" fill="none" stroke="#3277b5" stroke-width="1.6"/><ellipse cx="8" cy="8" rx="2.8" ry="6.5" fill="none" stroke="#3277b5" stroke-width="1.2"/><path d="M1.5 8h13" stroke="#3277b5" stroke-width="1.2"/></svg>
          www.quillmark.com
        </li>
      </ul>
    </div>
  </section>
</body>
</html>
```